creation of a postcard style drop off marketing vehicle..

WE GO LIVE

take a peek at my website to best understand my business. www.wegolive.com.

my business is recording young musicians (vocalist and instrumentalists) both video and audio. professional recordings produced at a price which a young artist can afford. i would like the postcard to help a prospect for my services to be able to visualize themselves performing in a recording studio. that, along with some titling which supports the image and provides contact data . i will use the postcard as both a drop off piece and as a piece to pin on a public announcement board. i need a business card which mimics the postcard with just contact data.

Professional and Affordable Video Recordings of Your Performance

High Quality Video Files (MPEG 4/H.264 Files) For Distribution Across
Internet, Social Media, Flickbay, Streamora, Or Embedding In Your Website.

www.WEGOLIVE.rocks

kelpbarn@mailnest.net
calvin brostoff
555-271-0846

```html
<!DOCTYPE html>
<html lang="en">
<head>
<meta charset="utf-8">
<title>WE GO LIVE – Postcard</title>
<link href="https://fonts.googleapis.com/css2?family=Raleway:wght@300;400;600&family=Oswald:wght@300;400;600&family=Lato:wght@400;700&display=swap" rel="stylesheet">
<style>
  :root {
    --ink: #0b0a09;
    --ink-soft: #1c1915;
    --gold-light: #d9b778;
    --gold: #b08a4c;
    --gold-deep: #6e5226;
    --paper: #ffffff;
    --backdrop: #e6e4e0;
    --rule: #8a8a8a;
    --studio-red: #8a2f12;
    --studio-orange: #c8601f;
  }
  * { margin: 0; padding: 0; box-sizing: border-box; }
  html, body { width: 853px; height: 1200px; overflow: hidden; }
  body { background: var(--backdrop); font-family: "Lato", sans-serif; position: relative; }

  .card { position: absolute; left: 26px; width: 800px; height: 512px; overflow: hidden; box-shadow: 0 4px 14px rgba(0,0,0,.25); }
  .card--front { top: 48px; background: var(--ink); }
  .card--back { top: 624px; background: var(--paper); }

  /* Front */
  .front-photo { position: absolute; left: 0; top: 0; width: 470px; height: 512px;
    background: radial-gradient(ellipse at 28% 38%, var(--studio-orange) 0%, var(--studio-red) 38%, #2a120a 70%, var(--ink) 100%); }
  .front-photo::after { content: ""; position: absolute; inset: 0; background: linear-gradient(90deg, rgba(11,10,9,0) 55%, var(--ink) 100%); }
  .brand-title { position: absolute; left: 322px; top: 30px; font-family: "Raleway", sans-serif; font-weight: 300;
    font-size: 64px; letter-spacing: 3px; color: var(--gold-light); white-space: nowrap; }
  .brand-sub { position: absolute; left: 322px; right: 30px; top: 122px; color: var(--paper); font-family: "Raleway", sans-serif; text-align: right; }
  .brand-sub .line-1 { font-size: 16px; font-weight: 600; letter-spacing: 1.2px; }
  .brand-sub .line-2 { font-size: 20px; font-weight: 400; letter-spacing: 4px; margin-top: 4px; }
  .offer-band { position: absolute; left: 0; top: 214px; width: 800px; height: 158px; }
  .offer-text { position: absolute; right: 34px; top: 222px; text-align: center; width: 360px; color: var(--ink); font-family: "Oswald", sans-serif; }
  .offer-text .o-top { font-size: 29px; font-weight: 300; letter-spacing: .5px; }
  .offer-text .o-main { font-size: 42px; font-weight: 600; line-height: 1.1; color: var(--paper); }
  .offer-text .o-bottom { font-size: 33px; font-weight: 300; line-height: 1.15; }
  .front-swoosh { position: absolute; left: 0; top: 400px; width: 800px; height: 112px; }
  .front-url { position: absolute; right: 34px; top: 450px; font-family: "Lato", sans-serif; font-weight: 700; font-size: 25px; color: var(--ink); }

  /* Back */
  .back-panel { position: absolute; left: 0; top: 0; width: 562px; height: 512px; background: var(--ink); }
  .back-strip { position: absolute; left: 0; top: 0; width: 562px; height: 512px; }
  .snapshot { position: absolute; border: 5px solid var(--paper); box-shadow: 0 3px 8px rgba(0,0,0,.5); }
  .snapshot--studio { left: 16px; top: 10px; width: 190px; height: 138px; transform: rotate(-4deg);
    background: linear-gradient(135deg, #8a6a48, #3d2e22 55%, #c9a27a); }
  .snapshot--stage { left: 18px; top: 180px; width: 188px; height: 134px; transform: rotate(-9deg);
    background: linear-gradient(160deg, #4a1c2e, #b8667a 45%, #2b1740); }
  .snapshot--camera { left: 22px; top: 364px; width: 170px; height: 122px; transform: rotate(5deg);
    background: linear-gradient(120deg, #cfc6b8, #4a423a 50%, #8c7f70); }
  .section { position: absolute; left: 214px; width: 330px; color: var(--paper); }
  .section h2 { font-family: "Raleway", sans-serif; font-weight: 400; font-size: 18px; color: var(--gold-light); letter-spacing: .5px; margin-bottom: 6px; text-transform: uppercase; }
  .section p { font-size: 10.6px; line-height: 1.38; text-align: justify; }
  .section--about { top: 30px; }
  .section--files { top: 195px; color: var(--ink); }
  .section--files h3 { font-family: "Oswald", sans-serif; font-weight: 400; font-size: 18px; }
  .section--files p { font-family: "Oswald", sans-serif; font-weight: 300; font-size: 13px; line-height: 1.3; text-align: left; }
  .section--videologues { top: 290px; }
  .contact-call { position: absolute; left: 214px; top: 466px; color: var(--ink); }
  .contact-call .label { font-family: "Oswald", sans-serif; font-size: 12px; font-weight: 400; letter-spacing: .4px; }
  .contact-call .phone { font-family: "Lato", sans-serif; font-weight: 700; font-size: 23px; line-height: 1; }
  .contact-web { position: absolute; left: 410px; top: 472px; font-size: 11px; line-height: 1.55; color: var(--ink); font-weight: 700; }
  .stamp-box { position: absolute; left: 686px; top: 35px; width: 86px; height: 86px; border: 1px solid var(--rule); }
  .address-line { position: absolute; left: 600px; width: 172px; height: 1px; background: var(--rule); }
</style>
</head>
<body>

<section class="card card--front">
  <div class="front-photo" role="img" aria-label="Long-haired bassist playing a white bass guitar in a recording studio with a softbox light behind him"></div>

  <svg class="offer-band" viewBox="0 0 800 158" preserveAspectRatio="none" aria-hidden="true">
    <defs>
      <linearGradient id="bandGold" x1="0" y1="0" x2="1" y2="0">
        <stop offset="0" stop-color="#6e5226"/>
        <stop offset=".35" stop-color="#d9b778"/>
        <stop offset=".7" stop-color="#b08a4c"/>
        <stop offset="1" stop-color="#6e5226"/>
      </linearGradient>
    </defs>
    <path d="M398 0 H800 V158 H398 Q372 158 380 130 L410 30 Q418 0 398 0 Z" fill="url(#bandGold)"/>
  </svg>

  <h1 class="brand-title">WE GO LIVE</h1>
  <div class="brand-sub">
    <div class="line-1">VIDEOGRAPHIC RECORDINGS FOR VOCALISTS</div>
    <div class="line-2">MUSICIANS AND THEATRE</div>
  </div>

  <div class="offer-text">
    <div class="o-top">PROFESSIONAL &amp; AFFORDABLE</div>
    <div class="o-main">VIDEO RECORDINGS</div>
    <div class="o-bottom">OF YOUR PERFORMANCE</div>
  </div>

  <svg class="front-swoosh" viewBox="0 0 800 112" preserveAspectRatio="none" aria-hidden="true">
    <defs>
      <linearGradient id="swooshGold" x1="0" y1="0" x2="1" y2="0">
        <stop offset="0" stop-color="#6e5226"/>
        <stop offset=".4" stop-color="#b08a4c"/>
        <stop offset=".8" stop-color="#d9b778"/>
        <stop offset="1" stop-color="#b08a4c"/>
      </linearGradient>
    </defs>
    <path d="M0 70 C180 60 340 40 440 6 L800 0 V112 H0 Z" fill="url(#swooshGold)"/>
    <path d="M0 62 C180 52 340 32 440 -2" fill="none" stroke="#d9b778" stroke-width="2"/>
  </svg>
  <div class="front-url">www.WEGOLIVE.rocks</div>
</section>

<section class="card card--back">
  <div class="back-panel"></div>
  <svg class="back-strip" viewBox="0 0 562 512" aria-hidden="true">
    <defs>
      <linearGradient id="stripGold" x1="0" y1="0" x2="1" y2="0">
        <stop offset="0" stop-color="#6e5226"/>
        <stop offset=".5" stop-color="#d9b778"/>
        <stop offset="1" stop-color="#8a6a34"/>
      </linearGradient>
    </defs>
    <rect x="70" y="0" width="120" height="512" fill="url(#stripGold)"/>
    <path d="M190 0 H562 V14 L540 28 H200 L190 18 Z" fill="url(#stripGold)"/>
    <path d="M190 190 H562 L548 226 L562 262 H190 Z" fill="url(#stripGold)"/>
    <path d="M190 454 H562 L548 483 L562 512 H190 Z" fill="url(#stripGold)"/>
  </svg>

  <div class="snapshot snapshot--studio" role="img" aria-label="Guitarist recording in a home studio"></div>
  <div class="snapshot snapshot--stage" role="img" aria-label="Theatre cast performing on a lit stage"></div>
  <div class="snapshot snapshot--camera" role="img" aria-label="Video camera on a tripod set up for a shoot"></div>

  <div class="section section--about">
    <h2>About Calvin Brostoff</h2>
    <p>I make my home in Maple Hollow, Vermont along with my wife Marla, my dog Biscuit, and my cat Pepper. After graduating from Northgate State University, I worked in the high tech marketplace for Corelane Systems, Quillbyte Equipment, and Dataspire. Upon leaving Dataspire in 2004, I began spending more time on my life-long avocation of photography and videography.</p>
  </div>

  <div class="section section--files">
    <h3>High Quality Video Files (MPEG 4/H.264 Files)</h3>
    <p>For Distribution Across Internet, Social Media, Flickbay, Streamora,<br>Or Embedding In Your Website.</p>
  </div>

  <div class="section section--videologues">
    <h2>Music Videologues</h2>
    <p>Music Videologues are a video musical story which explains the passion you have for music in order to give your audience a closer look into your work. These projects typically involve short interviews, several recorded musical segments, still photography and some historical memorabilia to hold the story together. The interviews and recordings are shot over one day and the material is edited into a 8 to 10 minute video the day following.</p>
  </div>

  <div class="contact-call">
    <div class="label">CALL CALVIN BROSTOFF</div>
    <div class="phone">555-271-0846</div>
  </div>
  <div class="contact-web">
    <div>kelpbarn@mailnest.net</div>
    <div>www.WEGOLIVE.rocks</div>
  </div>

  <div class="stamp-box"></div>
  <div class="address-line" style="top:310px"></div>
  <div class="address-line" style="top:345px"></div>
  <div class="address-line" style="top:380px"></div>
</section>

</body>
</html>
```